Business Strategy Company
Cards & Paper for Enterprise Collaboration Data Company
Project: Business Strategy Company
Business Strategy Company -
Creative Brief
Professional
Tobin G. Maraselt
CEO
31927 Harrowgate Ave. Suite 400 Berkley, CA 90388
tobin@quandelrox.example
www.quandelrox.example
Please include tagline: "Connected Work Insight" We would like a clean, modern card like the types found in these designs: https://www.pendlewick.example/drafts/display/contest/93587/draft/705568 https://www.pendlewick.example/drafts/display/contest/79787/draft/600578 https://www.pendlewick.example/drafts/display/contest/77433/draft/650842 https://www.pendlewick.example/drafts/display/contest/50102/draft/406651 https://www.pendlewick.example/drafts/display/contest/101628/draft/769948 https://www.pendlewick.example/drafts/display/contest/101641/draft/771307 https://www.pendlewick.example/drafts/display/contest/99022/draft/771303
We like a field of dark color or a gradient with the logo in either white or a color just slightly lighter/darker than the background (i.e. if the background is black, the logo would either be white or very dark gray). We'd like to see both.

```html
<!DOCTYPE html>
<html lang="en">
<head>
<meta charset="utf-8">
<title>Quandelrox Business Cards</title>
<link rel="stylesheet" href="https://fonts.googleapis.com/css2?family=Arimo:wght@400;700&display=swap">
<style>
  :root {
    --page: #d9d6d1;
    --white: #ffffff;
    --ink: #333333;
    --ink-soft: #555555;
    --accent: #1aa3c9;
    --accent-dark: #0b6f95;
    --rule: #c4c4c4;
    --navy-deep: #061634;
    --navy-mid: #0e5fa3;
    --black: #050505;
    --graphite: #3d3c3c;
    --graphite-dark: #1e1d1d;
    --pale: #e9eff5;
    --muted: #8c8c8c;
  }
  * { box-sizing: border-box; margin: 0; padding: 0; }
  html, body { width: 1200px; height: 720px; overflow: hidden; }
  body {
    background: var(--page);
    font-family: "Arimo", Arial, sans-serif;
    color: var(--ink);
  }
  .card-sheet {
    position: absolute; left: 154px; top: 96px;
    display: grid; grid-template-columns: 430px 430px; grid-template-rows: 250px 250px;
    column-gap: 32px; row-gap: 20px;
  }
  .card {
    position: relative; border-radius: 16px; overflow: hidden;
    box-shadow: 0 6px 14px rgba(0,0,0,.28);
  }
  .brand { display: flex; align-items: center; gap: 10px; }
  .brand-square { width: 20px; height: 20px; border-radius: 3px; flex: none; }
  .brand-name { font-weight: 400; letter-spacing: .5px; line-height: 1; }

  /* front */
  .card-front { background: var(--white); }
  .card-front .brand { position: absolute; left: 28px; top: 38px; }
  .card-front .brand-square { background: var(--navy-mid); }
  .card-front .brand-name { font-size: 30px; color: var(--ink); }
  .address { position: absolute; left: 236px; top: 140px; font-size: 9px; line-height: 1.45; color: var(--ink-soft); }
  .holder { position: absolute; left: 28px; top: 150px; }
  .holder-name { font-size: 15px; font-weight: 700; color: var(--ink); }
  .holder-role { font-size: 12px; color: var(--ink-soft); margin-top: 4px; }
  .contacts { position: absolute; left: 236px; top: 170px; font-size: 8.5px; line-height: 1.5; color: var(--ink-soft); list-style: none; }
  .contacts b { display: inline-block; width: 14px; color: var(--ink); }
  .front-band { position: absolute; left: 0; bottom: 0; width: 100%; height: 22px; }

  /* backs */
  .card-back { color: var(--pale); }
  .card-back .brand-square { background: currentColor; }
  .card-back .brand-name { font-size: 17px; }
  .back-blue { background: radial-gradient(ellipse at 58% 42%, var(--navy-mid) 0%, #0a3a74 45%, var(--navy-deep) 100%); }
  .back-black { background: var(--black); }
  .back-graphite { background: radial-gradient(ellipse at 50% 40%, var(--graphite) 0%, var(--graphite-dark) 100%); }
  .centered-brand { position: absolute; left: 0; right: 0; justify-content: center; }
  .back-blue .centered-brand { top: 94px; }
  .back-graphite .centered-brand { top: 78px; }
  .tagline-block { position: absolute; font-size: 10.5px; line-height: 1.55; letter-spacing: .4px; }
  .tagline-center { left: 0; right: 0; text-align: center; }
  .back-blue .tagline-center { top: 162px; }
  .back-graphite .tagline-center { top: 144px; }
  .tagline-left { left: 29px; top: 196px; color: var(--muted); }
  .faint-square { position: absolute; border-radius: 14px; }
  .back-blue .faint-square { right: 30px; top: 40px; width: 90px; height: 90px; background: rgba(255,255,255,.05); }
  .back-black .faint-square { left: 150px; top: 40px; width: 100px; height: 100px; background: rgba(255,255,255,.06); }
  .back-graphite .faint-square { left: 20px; top: 130px; width: 90px; height: 90px; background: rgba(255,255,255,.05); }
</style>
</head>
<body>
<main class="card-sheet">
  <section class="card card-front">
    <div class="brand"><span class="brand-square"></span><span class="brand-name">Quandelrox</span></div>
    <p class="address">31927 Harrowgate Ave. Suite 400<br>Berkley, CA 90388</p>
    <div class="holder">
      <p class="holder-name">Tobin G. Maraselt</p>
      <p class="holder-role">CEO</p>
    </div>
    <ul class="contacts">
      <li><b>P</b>555-201-4470</li>
      <li><b>C</b>555-318-2096</li>
      <li><b>F</b>555-642-7715</li>
      <li><b>E</b>tobin@quandelrox.example</li>
      <li><b>W</b>www.quandelrox.example</li>
    </ul>
    <svg class="front-band" viewBox="0 0 430 22" preserveAspectRatio="none" aria-hidden="true">
      <path d="M0 8 Q215 0 430 6 L430 22 L0 22 Z" fill="var(--rule)"/>
      <path d="M0 11 Q215 3 430 9 L430 22 L0 22 Z" fill="var(--accent)"/>
      <path d="M0 17 Q215 11 430 15 L430 22 L0 22 Z" fill="var(--accent-dark)"/>
    </svg>
  </section>

  <section class="card card-back back-blue">
    <span class="faint-square"></span>
    <div class="brand centered-brand"><span class="brand-square"></span><span class="brand-name">Quandelrox</span></div>
    <p class="tagline-block tagline-center">Connected Work Insight<br>www.quandelrox.example</p>
  </section>

  <section class="card card-back back-black">
    <span class="faint-square"></span>
    <p class="tagline-block tagline-left">Connected Work Insight<br>www.quandelrox.example</p>
  </section>

  <section class="card card-back back-graphite">
    <span class="faint-square"></span>
    <div class="brand centered-brand"><span class="brand-square"></span><span class="brand-name">Quandelrox</span></div>
    <p class="tagline-block tagline-center">Connected Work Insight<br>www.quandelrox.example</p>
  </section>
</main>
</body>
</html>
```